Re-Design WP Site BrightPebbles.info

Site Re-design. Also Need a Button for contact on main page. Need Great Looking products re designed. Also bonus if you can install a site SEO checker on the site.

BrightPebbles.info

```html
<!DOCTYPE html>
<html lang="en">
<head>
<meta charset="utf-8">
<title>Bright Pebbles – Digital Innovators</title>
<link href="https://fonts.googleapis.com/css2?family=Montserrat:wght@400;500;600;700;800&family=Open+Sans:wght@400;600&display=swap" rel="stylesheet">
<style>
:root{
  --purple:#6c61b8;
  --purple-dark:#5a4fa3;
  --purple-deep:#4d4392;
  --ink:#333344;
  --muted:#777788;
  --hero-bg:#f7f7fb;
  --page:#ffffff;
  --line:#e6e6ee;
  --media-dark:#1f1f22;
}
*{box-sizing:border-box;margin:0;padding:0}
html,body{width:1200px;height:2276px;overflow:hidden}
body{position:relative;background:var(--page);font-family:"Open Sans",Arial,sans-serif;color:var(--ink)}
.topbar{position:absolute;top:0;left:0;width:1200px;height:24px;background:var(--purple);display:flex;align-items:center;justify-content:center;gap:10px;color:#fff;font-size:10px}
.topbar .follow{margin-right:14px;font-family:"Montserrat",sans-serif}
.topbar .social{width:13px;height:13px;border-radius:50%;background:#fff}
.nav{position:absolute;top:24px;left:0;width:1200px;height:52px;background:#fff;box-shadow:0 1px 4px rgba(0,0,0,.06)}
.brand{position:absolute;left:225px;top:10px;font-family:"Montserrat",sans-serif;font-weight:700;font-size:16px;color:var(--purple-deep)}
.brand-line{position:absolute;left:225px;top:32px;width:90px;height:2px;background:var(--purple)}
.menu{position:absolute;right:220px;top:19px;display:flex;gap:28px;font-family:"Montserrat",sans-serif;font-size:11px;font-weight:600;color:var(--ink);list-style:none}
.menu .active{color:var(--purple);border-bottom:2px solid var(--purple);padding-bottom:4px}
.hero{position:absolute;top:76px;left:0;width:1200px;height:750px;background:var(--hero-bg)}
.hero h1{position:absolute;top:80px;width:100%;text-align:center;font-family:"Montserrat",sans-serif;font-weight:700;font-size:42px;color:var(--purple)}
.hero p{position:absolute;top:140px;left:420px;width:360px;text-align:center;font-size:13px;line-height:20px;color:var(--muted)}
.btn{display:inline-block;background:var(--purple);color:#fff;font-family:"Montserrat",sans-serif;font-weight:600;border-radius:20px;text-align:center}
.hero .btn{position:absolute;top:206px;left:500px;width:200px;height:34px;line-height:34px;font-size:10px;letter-spacing:.5px}
.video{position:absolute;top:420px;left:290px;width:620px;height:340px;background:linear-gradient(180deg,#2a2a2e,var(--media-dark))}
.video svg{position:absolute;left:278px;top:138px}
.shop-title{position:absolute;top:898px;width:100%;text-align:center;font-family:"Montserrat",sans-serif;font-weight:600;font-size:32px;color:var(--purple);letter-spacing:1px}
.shop-rule{position:absolute;top:945px;left:540px;width:120px;height:2px;background:var(--purple);opacity:.5}
.card{position:absolute;width:216px;background:#fff;box-shadow:0 2px 10px rgba(0,0,0,.12);padding:0 0 14px}
.card .media{height:196px;margin:8px 8px 0}
.card h3{margin:14px 12px 0;font-size:9.5px;line-height:14px;font-weight:600;color:var(--purple-deep);height:56px;overflow:hidden}
.card .price{margin:10px 12px 0;font-size:9px;line-height:13px;color:var(--muted)}
.card .price s{margin-right:4px}
.card .price b{color:var(--ink);font-weight:600}
.card .btn{margin:10px 12px 0;width:84px;height:22px;line-height:22px;font-size:8.5px;border-radius:12px}
.m1{background:linear-gradient(180deg,#e9e9ee,#c9c9d2)}
.m2{background:linear-gradient(135deg,#c94a3c,#d9c4a8 60%,#9fb08a)}
.m3{background:linear-gradient(135deg,#4f7a2c,#a7c46a 50%,#d79a8a)}
.m4{background:linear-gradient(135deg,#3c6b28,#8fb45a 60%,#c8d8a0)}
.m5{background:linear-gradient(180deg,#f4f4f4,#dfe6f2)}
.footer{position:absolute;top:1864px;left:0;width:1200px;height:386px;background:var(--purple);color:#fff}
.footer h2{position:absolute;left:225px;top:48px;font-family:"Montserrat",sans-serif;font-weight:700;font-size:24px}
.footer .tag{position:absolute;left:225px;top:80px;font-family:"Montserrat",sans-serif;font-weight:600;font-size:14px}
.footer .about{position:absolute;left:225px;top:106px;width:250px;font-size:8.5px;line-height:12px;opacity:.9}
.fnav{position:absolute;left:225px;top:222px;list-style:none;font-size:9px;line-height:20px;font-family:"Montserrat",sans-serif}
.fnav li::before{content:"";display:inline-block;width:8px;height:1px;background:#fff;vertical-align:middle;margin-right:16px}
.contact{position:absolute;left:645px;top:48px;width:360px}
.contact h2{position:static;font-size:24px;margin-bottom:14px}
.row{display:flex;gap:22px}
.field{flex:1;margin-bottom:10px}
.field label{display:block;font-size:8.5px;margin-bottom:3px}
.field .input{height:18px;background:#fff;border-radius:9px}
.field .area{height:80px;background:#fff;border-radius:8px}
.submit{display:inline-block;margin-top:4px;border:1px solid #fff;color:#fff;border-radius:12px;width:74px;height:20px;line-height:18px;text-align:center;font-size:8.5px;font-family:"Montserrat",sans-serif;font-weight:600}
.bottom{position:absolute;top:2250px;left:0;width:1200px;height:26px;background:var(--purple-dark);color:#fff;font-size:9px;text-align:center;line-height:26px}
</style>
</head>
<body>
<div class="topbar"><span class="follow">Follow Us</span><span class="social"></span><span class="social"></span><span class="social"></span></div>
<header class="nav">
  <div class="brand">Bright Pebbles</div>
  <div class="brand-line"></div>
  <ul class="menu"><li class="active">HOME</li><li>SHOP</li><li>SOLUTIONS</li><li>BLOG</li><li>CONTACT</li></ul>
</header>
<section class="hero">
  <h1>We Are Digital Innovators</h1>
  <p>We're a studio of creative thinkers making unique and effective IT applications providing solutions that solve real world problems.</p>
  <span class="btn">EXPLORE OUR WEBSPACE</span>
</section>
<div class="video" role="img" aria-label="Promotional video preview">
  <svg width="64" height="64" viewBox="0 0 64 64"><circle cx="32" cy="32" r="30" fill="none" stroke="#6c61b8" stroke-width="4"/><circle cx="32" cy="32" r="25" fill="#6c61b8"/><path d="M26 20 L44 32 L26 44 Z" fill="#2a2a2e"/></svg>
</div>
<h2 class="shop-title">SHOP</h2>
<div class="shop-rule"></div>

<article class="card" style="left:228px;top:1020px">
  <div class="media m1" role="img" aria-label="Digital display kiosk product photo"></div>
  <h3>#1 Social Media Marketing &amp; Local Listing Profile Boost – Monthly Price Included</h3>
  <p class="price"><s>$5,250.00</s><b>$3,460.00</b> / month and a $100.00 sign-up fee</p>
  <span class="btn">SIGN UP NOW</span>
</article>
<article class="card" style="left:484px;top:1020px">
  <div class="media m2" role="img" aria-label="Street map with location pin"></div>
  <h3>Digital Marketing – SEO Focus – Track Number of Visitors it Brings to Your Location – Know how to Your Competitors Customers – 50,000 Impressions</h3>
  <p class="price"><s>$1,200.00</s><b>$880.00</b> / month</p>
  <span class="btn">SIGN UP NOW</span>
</article>
<article class="card" style="left:752px;top:1020px">
  <div class="media m3" role="img" aria-label="Hemp plant leaves photo"></div>
  <h3>#1 Cannabis Advertising &amp; SEO Content Social Media Marketing &amp; Local Listing Boost – Monthly Price Included</h3>
  <p class="price"><s>$10,000.00</s><b>$9,750.00</b> / month</p>
  <span class="btn">SIGN UP NOW</span>
</article>
<article class="card" style="left:228px;top:1440px">
  <div class="media m4" role="img" aria-label="Hemp plant close-up photo"></div>
  <h3>Cannabis Targeted Display &amp; SEO Planning – Take Your Competitors Customers w/ 200,000 Impressions – Let Customers Order Your Brand</h3>
  <p class="price"><s>$5,250.00</s><b>$4,987.00</b> / month</p>
  <span class="btn">SIGN UP NOW</span>
</article>
<article class="card" style="left:484px;top:1440px">
  <div class="media m5" role="img" aria-label="Search results page with first page ranking headline"></div>
  <h3>Top Local SEO Ranking</h3>
  <p class="price"><s>$4,500.00</s><b>$3,900.00</b> / month</p>
  <span class="btn">SIGN UP NOW</span>
</article>

<footer class="footer">
  <h2>Bright Pebbles</h2>
  <div class="tag">We are Digital Innovators</div>
  <p class="about">Lorem ipsum is simply dummy text of the printing and typesetting industry. It has been the standard dummy text ever since, used by designers to show layout.</p>
  <ul class="fnav"><li>HOME</li><li>SHOP</li><li>SOLUTIONS</li><li>BLOG</li><li>CONTACT</li></ul>
  <div class="contact">
    <h2>CONTACT US</h2>
    <div class="row">
      <div class="field"><label>First Name</label><div class="input"></div></div>
      <div class="field"><label>Last Name</label><div class="input"></div></div>
    </div>
    <div class="field"><label>Email</label><div class="input"></div></div>
    <div class="field"><label>Comment or Message</label><div class="area"></div></div>
    <span class="submit">SUBMIT</span>
  </div>
</footer>
<div class="bottom">Copyright © Bright Pebbles</div>
</body>
</html>
```